Relationship Seminar

I am an Author and Speaker and I need a flyer for a Christian relationship seminar targeting women aged between mid 20's to late 30's. It's an event for women only.

-I am looking for a fresh/ edgy look but still feminine
-Nothing too girly
-Maximum of 3 colours (Spring colours are good)
-I want the flyer to convey joy or happiness
-Use my photo which is attached as the predominant image (you can crop it to remove the background etc)

The Flyer Details are as follows:

Somewhere Past Tomorrow - Brisbane Tour

Join Author & Speaker, Rosalind Okafe, as she speaks about her new book entitled 'Somewhere Past Tomorrow'.

Be inspired and encouraged to embrace the life that God has given you and make the most of it!

Date: Saturday 9th November 2013
Time: 2:00 pm - 5:00 pm
Location: Larkwell Hotel Brisbane (Juniper Ballroom)
Fennimore Street, Brisbane QLD 4000
Tickets: $60/pp (Includes High Tea)
Buy Tickets: www.rosalindokafe.com or http://somewherepasttomorrow.ticketvane.net

Email: info@rosalindokafe.com

Include the cover of my new book.

www.rosalindokafe.com (include my website at the bottom of the flyer)

Target Market(s)

Young professional women aged between their mid 20's to late 30's

Industry/Entity Type

Event

Requirements
Should not have
• -No girly or curly font

```html
<!DOCTYPE html>
<html lang="en">
<head>
<meta charset="utf-8">
<title>Somewhere Past Tomorrow – Brisbane Tour</title>
<link rel="stylesheet" href="https://fonts.googleapis.com/css2?family=Cinzel:wght@400;600;700&family=Open+Sans:wght@400;600;700&display=swap">
<style>
  :root {
    --orange: #ec6a22;
    --green: #8cc63f;
    --ink: #3a3a3a;
    --paper: #ffffff;
    --backdrop: #ece3d3;
  }
  * { margin: 0; padding: 0; box-sizing: border-box; }
  html, body {
    width: 1200px; height: 848px; overflow: hidden;
    background: var(--backdrop);
  }
  .flyer {
    position: absolute; left: 30px; top: 44px;
    width: 1140px; height: 760px;
    background: var(--paper);
    box-shadow: 0 6px 18px rgba(0,0,0,0.25);
    font-family: "Open Sans", Arial, sans-serif;
    color: var(--ink);
    overflow: hidden;
  }
  .speaker-photo {
    position: absolute; left: 560px; top: 0; width: 580px; height: 250px;
    background:
      linear-gradient(90deg, var(--paper) 0%, rgba(255,255,255,0.6) 22%, rgba(255,255,255,0) 48%),
      linear-gradient(135deg, #d9cfc6 0%, #c7a899 35%, #6b4a3c 62%, #2a211e 85%, #b8a69c 100%);
  }
  .title {
    position: absolute; font-family: "Cinzel", Georgia, serif;
    color: var(--orange); font-weight: 600; line-height: 1;
  }
  .title-line1 { left: 69px; top: 34px; font-size: 76px; }
  .title-line2 { left: 103px; top: 116px; font-size: 76px; }
  .tour {
    position: absolute; left: 172px; top: 196px;
    font-family: "Cinzel", Georgia, serif; font-weight: 600;
    font-size: 36px; color: var(--green); line-height: 1;
  }
  .intro {
    position: absolute; left: 30px; top: 256px; width: 1085px;
    font-size: 24.5px; font-weight: 700; line-height: 36px;
    text-indent: 40px;
  }
  .intro .speaker-name {
    font-family: "Cinzel", Georgia, serif; color: var(--orange);
    font-size: 29px; font-weight: 700;
  }
  .book-cover {
    position: absolute; left: 83px; top: 380px; width: 200px; height: 298px;
    background: linear-gradient(160deg, #f6f4ef 0%, #e4ded6 55%, #b9c79a 100%);
    box-shadow: 4px 4px 10px rgba(0,0,0,0.25);
  }
  .details {
    position: absolute; left: 367px; top: 398px;
    font-size: 25px; line-height: 35.8px; list-style: none;
  }
  .details .label { color: var(--green); font-weight: 700; }
  .details .cont-location { padding-left: 133px; }
  .details .cont-tickets { padding-left: 159px; }
  .web-band {
    position: absolute; left: 0; bottom: 0; width: 100%; height: 60px;
    background: var(--orange); color: var(--paper);
    font-family: "Cinzel", Georgia, serif; font-weight: 600;
    font-size: 38px; line-height: 60px; text-align: center;
    letter-spacing: 1px;
  }
</style>
</head>
<body>
  <main class="flyer">
    <div class="speaker-photo" role="img" aria-label="Portrait of the smiling author in a dark jacket against a whitewashed brick wall"></div>

    <h1>
      <span class="title title-line1">Somewhere</span>
      <span class="title title-line2">Past Tomorrow</span>
    </h1>
    <p class="tour">Brisbane Tour</p>

    <p class="intro">Join Author &amp; Speaker, <span class="speaker-name">Rosalind Okafe</span>, as she speaks about her new book entitled 'Somewhere Past Tomorrow'. Be inspired and encouraged to embrace the life that God has given you and make the most of it!</p>

    <div class="book-cover" role="img" aria-label="Book cover of Somewhere Past Tomorrow showing a woman in a white dress between two men"></div>

    <ul class="details">
      <li><span class="label">Date:</span> Saturday 9th November 2013</li>
      <li><span class="label">Time:</span> 2:00 pm - 5:00 pm</li>
      <li><span class="label">Location:</span> Larkwell Hotel Brisbane (Juniper Ballroom)</li>
      <li class="cont-location">Fennimore Street, Brisbane QLD 4000</li>
      <li><span class="label">Tickets:</span> $60/pp (Includes High Tea)</li>
      <li><span class="label">Buy Tickets:</span> www.rosalindokafe.com or</li>
      <li class="cont-tickets">http://somewherepasttomorrow.ticketvane.net</li>
      <li><span class="label">Email:</span> info@rosalindokafe.com</li>
    </ul>

    <footer class="web-band">www.rosalindokafe.com</footer>
  </main>
</body>
</html>
```